" Clínica médica que atua nas diversas especialidades e realiza atendimentos particulares a preços acessíveis, podendo futuramente atender planos de saúde. "

```html
<!DOCTYPE html>
<html lang="pt-BR">
<head>
<meta charset="utf-8">
<title>Vivere Saúde — Consultas e Tratamentos</title>
<link rel="stylesheet" href="https://fonts.googleapis.com/css2?family=Raleway:wght@300;400;500&family=Montserrat:wght@600;800;900&display=swap">
<style>
  :root{
    --green-deep:#0d4a33;
    --green-dark:#135c3e;
    --green-mid:#1f7a4c;
    --green-band:#4fae55;
    --green-soft:#7fcf6e;
    --hero-bg:#eceef1;
    --white:#ffffff;
    --ink:#1d2b27;
    --ink-soft:#4a5552;
    --blue-line:#2a7fc2;
    --page-bg:#f4f4f4;
  }
  *{margin:0;padding:0;box-sizing:border-box}
  html,body{width:1200px;height:1200px;overflow:hidden;background:var(--page-bg)}
  body{font-family:"Raleway",sans-serif;color:var(--ink)}
  a{text-decoration:none}
  .site{position:absolute;top:250px;left:0;width:1200px;height:700px;background:var(--white);overflow:hidden}

  .header{display:flex;height:98px}
  .brand{width:223px;background:linear-gradient(180deg,var(--green-mid),var(--green-deep));display:flex;flex-direction:column;justify-content:center;align-items:center;gap:4px}
  .brand-name{display:flex;align-items:center;gap:8px;font-family:"Montserrat",sans-serif;font-weight:600;font-size:22px;color:var(--white)}
  .brand-dot{width:14px;height:14px;border-radius:50%;background:var(--white)}
  .brand-tag{font-size:10px;color:var(--white);letter-spacing:.5px;opacity:.85}

  .nav-area{flex:1;display:flex;flex-direction:column}
  .info-strip{height:30px;display:flex;justify-content:space-between;align-items:center;padding:0 22px;font-size:9px;color:var(--ink-soft);border-bottom:1px solid #e3e6e8}
  .nav{flex:1;display:flex;align-items:center;justify-content:space-around;padding:0 10px;border-bottom:4px solid transparent;border-image:linear-gradient(90deg,var(--green-mid),var(--blue-line)) 1}
  .nav a{font-weight:500;font-size:17px;color:var(--ink);text-align:center;line-height:1.15}

  .results-btn{width:223px;background:linear-gradient(180deg,var(--green-mid),var(--green-deep));color:var(--white);font-family:"Montserrat",sans-serif;font-weight:800;font-size:17px;text-align:center;display:flex;align-items:center;justify-content:center;line-height:1.2}

  .hero{position:relative;height:483px;background:var(--hero-bg)}
  .hero-text{position:absolute;left:56px;top:70px}
  .hero-title{font-family:"Montserrat",sans-serif;font-weight:900;font-size:42px;line-height:1.25;color:var(--green-deep);letter-spacing:.5px}
  .hero-sub{margin-top:16px;font-weight:300;font-size:44px;line-height:1.2;color:var(--green-dark)}
  .hero-body{margin-top:26px;font-weight:400;font-size:19px;line-height:1.3;color:var(--ink-soft)}
  .hero-photo{position:absolute;right:55px;bottom:0;width:420px;height:420px;background:radial-gradient(ellipse at 50% 60%,#ffffff 0%,#dfe3e6 70%,var(--hero-bg) 100%)}

  .divider{height:6px;background:linear-gradient(90deg,var(--green-mid),var(--blue-line) 50%,var(--green-mid))}

  .specialties{position:relative;height:113px;background:linear-gradient(180deg,var(--green-soft),var(--green-band))}
  .specialties-title{position:absolute;left:600px;top:30px;font-family:"Montserrat",sans-serif;font-weight:900;font-size:36px;line-height:1;color:var(--green-deep);letter-spacing:.5px}
  .specialties-photo{position:absolute;left:300px;top:20px;width:150px;height:93px;border-radius:10px 10px 0 0;background:linear-gradient(180deg,#c9a893,#3d4a56)}
</style>
</head>
<body>
  <main class="site">
    <header class="header">
      <div class="brand">
        <div class="brand-name"><span class="brand-dot"></span>Vivere Saúde</div>
        <div class="brand-tag">clínica médica</div>
      </div>
      <div class="nav-area">
        <div class="info-strip">
          <span>Seg a Sex das 7h às 19h</span>
          <span>Rua das Acácias, 120 - Centro</span>
          <span>contato@clinicavivere.com.br</span>
          <span>(00) 0000-0000</span>
        </div>
        <nav class="nav">
          <a href="#">Quem Somos</a>
          <a href="#">Consultas<br>e Tratamentos</a>
          <a href="#">Exames</a>
          <a href="#">Fale Conosco</a>
        </nav>
      </div>
      <a class="results-btn" href="#">RESULTADOS<br>DE EXAMES</a>
    </header>

    <section class="hero">
      <div class="hero-text">
        <h1 class="hero-title">CONSULTAS E<br>TRATAMENTOS</h1>
        <p class="hero-sub">Relação de especialidades<br>e tratamento oferecidos</p>
        <p class="hero-body">Temos diversas especialidades e o melhor tratamento<br>com exelentíssimos profissinais.</p>
      </div>
      <div class="hero-photo" role="img" aria-label="Foto de médico sorridente de jaleco branco com estetoscópio segurando uma prancheta"></div>
    </section>

    <div class="divider"></div>

    <section class="specialties">
      <div class="specialties-photo" role="img" aria-label="Foto de profissional de saúde, parcialmente visível"></div>
      <h2 class="specialties-title">ESPECIALIDADES</h2>
    </section>
  </main>
</body>
</html>
```